Cognitive therapist.

I am a therapist and my main work is with clients who have depression and anxiety disorders.

I need something reasonably plain. Cognitive therapy is a very pragmatic approach to dealing with problems, so it isn't new agey (no offence to new age therapies at all)

Hi everyone, I am currently looking at a particular design that I will most likely go with. Cheers, Lyn

Lyn Marchet
Cognitive Therapist
BA, PG Dip Mental Health,
PG Dip Cog Beh Therapy
MKRPG

The Quillan Rooms,
Level One
47 Harwick Parade
Cnr Drayfield St & Harwick Parade
P O Box 38 215
WELLINGTON 6287

Phone: 027 463 2851 Email: lmarchet@quorvane.co.nz

www.lynmarchet.co.nz

• No illustration, or colour. not old style fonts.

```html
<!DOCTYPE html>
<html lang="en">
<head>
<meta charset="utf-8">
<title>Lyn Marchet – Business Card</title>
<link rel="stylesheet" href="https://fonts.googleapis.com/css2?family=Open+Sans:wght@400;600;700&display=swap">
<style>
  :root {
    --backdrop: #ececec;
    --paper-light: #ffffff;
    --paper-shade: #e6e4e1;
    --brand-blue: #1a9fd6;
    --band-blue-light: #2a8fde;
    --band-blue-dark: #0d5fae;
    --silver-light: #f2f2f2;
    --silver-dark: #9a9a9a;
    --ink: #3f3f3f;
    --white: #ffffff;
    --portrait-light: #bdbdbd;
    --portrait-dark: #5a5a5a;
  }
  * { box-sizing: border-box; margin: 0; padding: 0; }
  html, body {
    width: 1200px;
    height: 864px;
    overflow: hidden;
    background: var(--backdrop);
    font-family: "Open Sans", Arial, sans-serif;
  }
  .card {
    position: absolute;
    left: 40px;
    top: 128px;
    width: 1120px;
    height: 608px;
    overflow: hidden;
    background: linear-gradient(90deg, var(--paper-shade) 0%, var(--paper-light) 55%);
  }
  .card__shapes {
    position: absolute;
    inset: 0;
  }
  .portrait {
    position: absolute;
    left: 0;
    top: 32px;
    width: 351px;
    height: 576px;
    background: linear-gradient(160deg, var(--portrait-light) 0%, var(--portrait-dark) 100%);
  }
  .identity {
    position: absolute;
    left: 351px;
    top: 44px;
  }
  .identity__name {
    font-size: 64px;
    font-weight: 600;
    color: var(--brand-blue);
    line-height: 1;
    letter-spacing: 0.5px;
  }
  .identity__credentials {
    margin-top: 26px;
    font-size: 23px;
    line-height: 29px;
    color: var(--ink);
  }
  .contact {
    position: absolute;
    right: 84px;
    top: 258px;
    list-style: none;
    text-align: right;
  }
  .contact__item {
    display: flex;
    justify-content: flex-end;
    align-items: center;
    gap: 12px;
    height: 40px;
    font-size: 23px;
    font-weight: 600;
    color: var(--white);
  }
  .contact__icon {
    width: 30px;
    height: 30px;
    flex: none;
  }
  .address {
    position: absolute;
    right: 94px;
    top: 462px;
    font-size: 21px;
    line-height: 36px;
    color: var(--white);
    text-align: right;
    font-style: normal;
  }
</style>
</head>
<body>
  <main class="card">
    <svg class="card__shapes" viewBox="0 0 1120 608" width="1120" height="608" aria-hidden="true">
      <defs>
        <linearGradient id="silverBand" x1="0" y1="0" x2="1" y2="0">
          <stop offset="0" stop-color="var(--silver-light)"/>
          <stop offset="0.6" stop-color="var(--silver-dark)"/>
          <stop offset="1" stop-color="var(--silver-light)"/>
        </linearGradient>
        <linearGradient id="blueField" x1="0" y1="0" x2="1" y2="1">
          <stop offset="0" stop-color="var(--band-blue-light)"/>
          <stop offset="1" stop-color="var(--band-blue-dark)"/>
        </linearGradient>
      </defs>
      <path class="silver-band" d="M758,0 C750,260 640,500 426,608 L520,608 C700,480 772,250 776,0 Z" fill="url(#silverBand)"/>
      <path class="blue-field" d="M776,0 C772,250 700,480 520,608 L1120,608 L1120,0 Z" fill="url(#blueField)"/>
    </svg>

    <div class="portrait" role="img" aria-label="Black and white portrait photo of the therapist"></div>

    <header class="identity">
      <h1 class="identity__name">Lyn Marchet</h1>
      <p class="identity__credentials">Cognitive Therapist BA,<br>PG Dip Mental Health,<br>PG Dip Cog Beh Therapy</p>
    </header>

    <ul class="contact">
      <li class="contact__item">027 463 2851
        <svg class="contact__icon" viewBox="0 0 30 30" aria-hidden="true">
          <circle cx="15" cy="15" r="14" fill="#dfe9f3"/>
          <path d="M9 8 l4 0 l1.5 4 l-2 1.5 c1 2 2.5 3.5 4.5 4.5 l1.5 -2 l4 1.5 l0 4 c-8 1 -14 -5 -13.5 -13.5 z" fill="#1d5f9e"/>
        </svg>
      </li>
      <li class="contact__item">lmarchet@quorvane.co.nz
        <svg class="contact__icon" viewBox="0 0 30 30" aria-hidden="true">
          <rect x="3" y="7" width="24" height="17" rx="2" fill="#dfe9f3"/>
          <path d="M3.5 8 L15 17 L26.5 8" fill="none" stroke="#1d5f9e" stroke-width="2"/>
        </svg>
      </li>
      <li class="contact__item">www.lynmarchet.co.nz
        <svg class="contact__icon" viewBox="0 0 30 30" aria-hidden="true">
          <circle cx="15" cy="15" r="13" fill="#7cc3ea" stroke="#dfe9f3" stroke-width="2"/>
          <ellipse cx="15" cy="15" rx="5.5" ry="13" fill="none" stroke="#ffffff" stroke-width="1.5"/>
          <path d="M2 15 H28 M4.5 9 H25.5 M4.5 21 H25.5" stroke="#ffffff" stroke-width="1.5"/>
        </svg>
      </li>
    </ul>

    <address class="address">
      MKRPG The Quillan Rooms, Level<br>
      One 47 Harwick Parade Cnr Drayfield St &amp;<br>
      Harwick Parade P O Box 38 215<br>
      WELLINGTON 6287
    </address>
  </main>
</body>
</html>
```